author needs a Book Cover design

Needs a book cover design that matches the title in some way.
Book Title is- 9 Lanterns Beneath a Quiet Harbor Tonight.
Subtile- Harvest Lessons Across Ordinary Seasons.
Author Name:-Desmond Okorefe, Jr.

Final Design is subject to Book Publisher's requirement.

Font styles to use
Serif

Requirements
Must have
• Follow these recommended specifications for your cover file:
• Page Size: Your cover should be a single (one-piece) PDF that includes the back cover, spine, and front cover. You can submit your cover on any size page as long as the printable area is measured exactly for your book's trim size, spine width, and allows at least .125” bleed, centered horizontally and vertically.
• Minimum Cover Width: Bleed + Back Cover Trim Size + Spine Width + Front Cover Trim Size + Bleed
• Minimum Cover Height: Bleed + Book Height Trim Size + Bleed
• Trim Size: Your cover should be the same trim size as you choose in the Title Information when setting up your book. For example, submitting a cover that was previously used for a 6.25” x 9.25” book would not work for a 6” x 9” book.
• Barcodes: For manufacturing and distribution reasons, your book's back cover must include a valid ISBN barcode. If your cover already has an ISBN barcode, make sure it is high-resolution, or at least 300 dpi, and 1.5" - 2" in width with proportional height. Ideally, this barcode should be 2” wide by 1.2” tall. Also, check to make sure you have the rights to use the ISBN on your cover, because not all services allow you to use their ISBNs elsewhere.
• QR codes: There are no set size restrictions, but the quality (resolution) of the image must be set to at least 300 dpi. Make sure you have the rights to use the code.
• If your artwork does not include a barcode, we will automatically add one in the lower right-hand corner of your book's back cover, free of charge. Our system will place the ISBN barcode in a space 2" wide and 1.2" tall. The bottom of this barcode is located 1/4" up from the bottom trim line of the cover. The right side of the barcode is located 1/4" to the left of the spine. Please ensure that you don't have any important images or text in the barcode location. You can also refer to our Artwork Templates for the exact size and position of the ISBN barcode on your final cover.
• If you don’t have an ISBN already on your cover, but you have live graphic or text elements in the location that our system will place the ISBN, you will need to move those elements or place the ISBN in a different location yourself.
• Publishing Logos: We do not add our logo to your book.
• Spine Width and Variance: If your artwork was created for a different service, please make sure that the spine width of your current cover matches our spine width. Different services may use different paper thickness, which is why the spine width of your cover artwork could be correct for another service but incorrect for our service.
• Ideally, you should avoid hard vertical lines separating your front or back cover panels from your spine and should allow for at least a .125" variance of your spine on each side (for example, the text on a 1" spine should be no larger than .75" wide). For books with a page count of less than 130 pages, we strongly recommend a blank spine.
• Your spine width should be calculated based on the number of pages in your book and using the appropriate formula:
• Black and White Interior Book Spine Width:
• White paper: Number of pages x .002252 = Spine width in inches
• Cream paper: Number of pages x .0025 = Spine width in inches
• Color Interior Book Spine Width:
• Number of pages x .002347 = Spine width in inches
• Example of spine width calculation for a 120-page black and white interior book with white paper:
• 120 x .002252 = .27" spine width
• Text and Image Placement: All live cover elements, or text and images that cannot be cut, must be at least .125" inside the trim lines to ensure no important elements are cut during the bookmaking process and the appearance of your printed books is consistent.
• Bleed: Your cover's background must extend at least .125" beyond the final trim line to accommodate for cutting/trimming tolerance.
• Crop/Registration Marks: Please do not include any crop or registration marks on your files, as they may interfere with the binding process or appear on the cover. We use our own measurements, specific to our systems, for cutting and binding; crop or registration marks placed by you could interfere with this process.
• Images and Fonts: Any images you include on your book's cover may be tagged with your choice of CMYK or RGB profiles or left untagged in a generic color space. All images should be sized at 100%, flattened to one layer and placed in your native document at a resolution of at least 300 DPI. You should also embed all fonts in your PDF file.
• Desmond, I hope this information is helpful to you. Please feel free to contact us if you have any other questions or concerns.
• Best regards,
• *WILL SUPPLY THE PAGE NUMBERS INFORMATION
• Lisbeth
• PrintHollow Member Services
Nice to have
• An attractive design that matches the title. Design can include backgrounds

```html
<!DOCTYPE html>
<html lang="en">
<head>
<meta charset="utf-8">
<title>9 Lanterns Beneath a Quiet Harbor Tonight — Cover</title>
<link rel="stylesheet" href="https://fonts.googleapis.com/css2?family=Tinos:ital,wght@0,400;0,700;1,400&family=Allura&display=swap">
<style>
  :root {
    --cream: #fbf7ea;
    --paper: #ffffff;
    --umber: #7a5c2a;
    --ink: #1b1611;
    --title-shadow: rgba(40, 25, 10, 0.75);
  }
  * { margin: 0; padding: 0; box-sizing: border-box; }
  html, body { width: 1200px; height: 743px; overflow: hidden; background: var(--cream); }
  .cover {
    position: relative;
    width: 1200px;
    height: 743px;
    overflow: hidden;
    font-family: "Tinos", "Times New Roman", serif;
    color: var(--ink);
  }
  .cover-art {
    position: absolute;
    inset: 0;
    background:
      radial-gradient(ellipse 190px 190px at 888px 384px, rgba(255, 214, 110, 0.9), rgba(226, 169, 58, 0.55) 45%, rgba(226, 169, 58, 0) 100%),
      radial-gradient(ellipse 150px 260px at 690px 300px, rgba(60, 40, 20, 0.85), rgba(74, 53, 32, 0.4) 55%, rgba(74, 53, 32, 0) 100%),
      radial-gradient(ellipse 260px 180px at 820px 680px, rgba(232, 170, 60, 0.85), rgba(232, 170, 60, 0) 100%),
      radial-gradient(ellipse 260px 220px at 1140px 560px, rgba(201, 134, 31, 0.7), rgba(201, 134, 31, 0) 100%),
      radial-gradient(ellipse 120px 420px at 0px 400px, rgba(90, 70, 40, 0.55), rgba(90, 70, 40, 0) 100%),
      linear-gradient(100deg, #fdfbf4 0%, #f6efdc 40%, #b89566 56%, #d8ad62 72%, #f1ddb0 100%);
  }
  .back-panel {
    position: absolute;
    left: 65px;
    top: 65px;
    width: 413px;
    height: 612px;
    background: var(--paper);
  }
  .back-blurb {
    position: absolute;
    left: 11px;
    top: 11px;
    width: 389px;
    height: 236px;
    background: var(--umber);
    color: var(--paper);
    padding: 14px 33px 0 26px;
    font-size: 10.6px;
    line-height: 13.7px;
    text-align: justify;
  }
  .back-blurb p { text-indent: 36px; margin-bottom: 13px; }
  .back-blurb .signature { text-align: right; text-indent: 0; margin: -13px 12px 0 0; }
  .author-bio {
    position: absolute;
    left: 37px;
    top: 257px;
    width: 244px;
    font-size: 12.4px;
    line-height: 15.4px;
    text-align: justify;
  }
  .author-bio strong { font-weight: 700; }
  .author-photo {
    position: absolute;
    left: 295px;
    top: 260px;
    width: 72px;
    height: 72px;
    background: linear-gradient(180deg, #c9a46a 0%, #8a6a44 55%, #e7e2da 100%);
  }
  .spine-title {
    position: absolute;
    left: 556px;
    top: 128px;
    height: 450px;
    writing-mode: vertical-rl;
    font-family: "Allura", cursive;
    font-weight: 400;
    font-size: 42px;
    line-height: 46px;
    color: var(--paper);
    text-shadow: 0 0 3px var(--title-shadow);
    white-space: nowrap;
  }
  .front-title {
    position: absolute;
    left: 688px;
    top: 62px;
    width: 440px;
    font-family: "Allura", cursive;
    font-weight: 400;
    font-size: 62px;
    line-height: 78px;
    color: var(--paper);
    text-align: right;
    text-shadow: 1px 2px 3px var(--title-shadow);
  }
  .front-subtitle {
    position: absolute;
    left: 700px;
    top: 302px;
    width: 424px;
    font-size: 23px;
    color: var(--paper);
    text-align: right;
    text-shadow: 0 1px 2px var(--title-shadow);
    white-space: nowrap;
  }
</style>
</head>
<body>
<main class="cover">
  <div class="cover-art" role="img" aria-label="Smoky golden background with a glowing lantern light over dark harbor haze"></div>

  <section class="back-panel">
    <div class="back-blurb">
      <p>A full and fruitful life grows when we listen to God’s Word and then live it out day by day. Scripture returns to this idea again and again: the reward is found not only in hearing, but in doing. Those who receive the word and act on it are called blessed (Luke 11:28), and knowing the truth brings joy when we carry it into our own steps (John 13:17).</p>
      <p>This book invites every reader to take these timeless covenant lessons into ordinary life, making small and steady choices to walk in them each season. To taste the abundant life promised in John 10:10, a believer must become a doer and not a listener only. Living the Word is a tested path toward a steady and victorious walk. May these pages light your way toward your covenant calling.</p>
      <p class="signature">Dr. Desmond Okorefe, Jr.</p>
    </div>
    <div class="author-photo" role="img" aria-label="Portrait photo of the author"></div>
    <p class="author-bio"><strong>DESMOND OKOREFE, JR. Ph.D.</strong>, is Senior Pastor of the Stillwater Bible Fellowship Church, Marlow Springs, Ohio. A visionary and a missionary, he has traveled extensively, preaching and lecturing in several countries, and has studied and demonstrated proficiency in various fields such as Theology, Education, Christian Counseling, Writing, Speaking and Applied Sciences, (Biochemistry, Bacteriology &amp; Public Health). Dr. Okorefe is author of online daily devotions, ‘Morning Wellspring’, and President of RISE-BROTHERS+, an International Ministry to Men. He is president of Stillwater International Christian Ministries and Protestant Minister, for the Ridgefield County Department of Rehabilitation and is an ordained Bishop with the FGCA Ministries, (Fellowship of Grace Covenant Assemblies, USA). He is blessed with his wife Pastor Amara and their four children.</p>
  </section>

  <h2 class="spine-title">9 Lanterns Beneath a Quiet<br>Harbor Tonight</h2>

  <h1 class="front-title">9 Lanterns Beneath<br>a Quiet Harbor<br>Tonight</h1>
  <p class="front-subtitle">Harvest Lessons Across Ordinary Seasons</p>
</main>
</body>
</html>
```